CSS design for a web application

We are currently building a web application in JAVA. The application uses a combination of a HTML template and CSS for the look and feel. We currenly have a very corporate look and feel for demo puposes, but we need to have some CSS designs that we can show to prospective customers. One of the functionalities of our application is the possibility to upload a customer's own (CSS) design in the application.

Our first customer is a high school in The Netherlands (12-18 year students) for children who are physically challenged. So the design should be easy to read, buttons should be easy to see, read and click and the different parts/texts on the website shouldn't be too close together. At the same time, we would like to avoid too much scrolling (especially horizontally). Go with a minimun screen resolution of 1024 x 768.

As our users are children, nice colours and other fun elements would be nice, while keeping a 'school like' appearance. Please use pictures and icons that our users will relate too. We want to communicate that our software is easy, fun and at the same time professional.

Our product is based on Brindle Suite by Brindle and thus Brindle applications as Postrix, Calendar, Brindle Pages etc are all integrated in our software solution.

Find attached a static HTML file that contains our current CSS design. This should be used as a basis as it contains al the CSS elements that are used in the application. Please note that jQuery (javascript) knowledge is necessary.

Target Market(s)

Students at high school (age group 12/13 to 17/18). Users have physical disabilities that sometimes means they need special equipment/tools to operate their laptop.

Requirements
Must have
• Easy too navigate, buttons that are easy to see/use
Nice to have
• 'WOW' factor when people look at the design
Should not have
• buttons/text that is too small, too close together

```html
<!DOCTYPE html>
<html lang="en">
<head>
<meta charset="utf-8">
<title>Skylark – Study Guide</title>
<link href="https://fonts.googleapis.com/css2?family=Arimo:wght@400;700&display=swap" rel="stylesheet">
<style>
:root{
  --sky:#4fb3e0;
  --sky-dark:#2b8fc4;
  --sky-light:#bfe6f7;
  --navy:#1d3f5c;
  --tab-dark:#1f4f74;
  --tab-mid:#2f7bab;
  --panel:#e6f3f9;
  --panel-line:#c9e3ef;
  --link:#1a9ad6;
  --text:#2a2a2a;
  --muted:#6f8694;
  --cyan:#45c6ec;
  --white:#ffffff;
  --green:#7aa31c;
}
*{box-sizing:border-box;margin:0;padding:0}
html,body{width:1053px;height:1200px;overflow:hidden}
body{font-family:"Arimo",Arial,sans-serif;color:var(--text);position:relative;
  background:linear-gradient(#f2f4f5,#ffffff 60%,#e9edef);}
.abs{position:absolute}
.topbar{left:0;top:0;width:1053px;height:132px;background:linear-gradient(#5fbde6,#3fa6d8 80%,#7ccbee)}
.topbar-bottom{left:0;top:132px;width:1053px;height:10px;background:linear-gradient(#d6ecf6,#f4f8fa)}
.logo-box{left:13px;top:13px;width:324px;height:105px;background:linear-gradient(#fff,#eef3f6);border-radius:5px;box-shadow:0 1px 4px rgba(0,0,0,.25);display:flex;align-items:center;padding-left:34px;gap:16px}
.logo-dot{width:34px;height:34px;border-radius:50%;background:var(--sky-dark)}
.logo-name{font-size:44px;font-weight:700;color:#3a3a3a;letter-spacing:-1px}
.account{left:803px;top:0;width:250px;height:132px;border-left:1px solid rgba(255,255,255,.35);padding:14px 0 0 12px;font-size:13px;color:#173449;background:rgba(255,255,255,.06)}
.account b{font-weight:700}
.account .links{margin-top:6px;font-size:12px;color:#fff;display:flex;gap:6px;align-items:center}
.account .msgs{margin-top:6px;font-size:12px;color:#fff;font-weight:700;display:flex;gap:6px;align-items:center}
.account .meta{margin-top:16px;font-size:10px;color:#2c5d7c;line-height:13px}
.search{left:842px;top:125px;width:198px;height:48px;background:#f4f6f7;border:1px solid #cfd8dd;padding:5px}
.search .field{height:22px;border:1px solid #bcc6cc;background:#fff;border-radius:3px;display:flex;align-items:center;justify-content:space-between;padding:0 3px 0 6px}
.search .go{font-size:10px;font-weight:700;background:#dfe8ed;border:1px solid #9ab;padding:1px 4px;border-radius:2px}
.search .label{font-size:10px;color:#456;margin-top:3px}
.tab{top:142px;height:34px;border-radius:4px 4px 0 0;background:linear-gradient(var(--tab-mid),var(--tab-dark));color:#fff;font-weight:700;font-size:14px;display:flex;align-items:center;justify-content:center}
.tab.active{background:linear-gradient(#e6f3f8,#a9d6ea);color:var(--navy);top:140px;height:38px}
.subnav{left:0;top:179px;width:1053px;height:42px;background:linear-gradient(#3fb1e2,#2d9fd2);display:flex;align-items:center;gap:22px;padding-left:19px;color:#fff;font-size:13px}
.subnav span{display:flex;align-items:center;gap:4px}
.footer{left:0;top:1151px;width:1053px;height:49px;background:linear-gradient(#3a9fd2,#62bce6);border-top:2px solid #2a6f98}
.card{border:1px solid #8fc8e2;border-radius:6px;overflow:hidden}
.clock{left:13px;top:247px;width:245px;height:269px;background:linear-gradient(#47b9e6,#2f9fd3);border-color:#1f7aa8}
.clock .time{text-align:center;color:#fff;font-size:34px;margin-top:10px}
.clock .date{text-align:center;color:#0f2b3e;font-size:14px;margin-top:4px}
.cal{position:absolute;left:10px;top:82px;width:223px;height:180px;border-radius:5px;background:rgba(255,255,255,.15)}
.cal .month{text-align:center;font-weight:700;font-size:13px;color:#0f2b3e;margin-top:8px}
.cal .heads,.cal .grid{display:grid;grid-template-columns:repeat(7,24px);column-gap:4.5px;position:absolute;left:14px}
.cal .heads{top:28px;font-size:10px;font-weight:700;color:#fff;text-align:center}
.cal .grid{top:49px;row-gap:4.5px}
.cal .grid span{height:22px;background:#1e3f55;color:#fff;font-size:11px;font-weight:700;display:flex;align-items:center;justify-content:center;border:1px solid #6fb8d8}
.cal .grid .empty{background:#3d7d9b}
.cal .grid .today{background:#6ec6ea;color:#12354d;border-color:#fff}
.event-row{left:13px;top:518px;width:245px;height:24px;background:#dbe6ec;display:flex;justify-content:space-around;align-items:center;font-size:11px;color:#355}
.event-row span{display:flex;gap:4px;align-items:center}
.box-head{height:37px;background:linear-gradient(#5c8fae,#2f6688);color:#fff;font-size:20px;padding:8px 0 0 14px}
.sidebar{left:13px;top:562px;width:245px;height:243px;background:var(--cyan)}
.sidebar li{list-style:none;height:29.5px;border-bottom:1px solid #3ab4dc;font-size:12px;color:#1b4861;display:flex;align-items:center;padding-left:14px;gap:8px}
.sidebar li::before{content:"";border-left:4px solid #2b7aa1;border-top:3px solid transparent;border-bottom:3px solid transparent}
.todo{left:13px;top:826px;width:245px;height:306px;background:linear-gradient(#d9ecf4,#c3dfeb)}
.todo .item{padding:9px 14px 6px 16px;border-bottom:1px solid #a8cedd}
.todo .title{font-weight:700;font-size:13px;color:#1a3a50;display:flex;align-items:center;gap:8px}
.todo .num{width:15px;height:15px;border-radius:50%;background:var(--green);color:#fff;font-size:10px;display:flex;align-items:center;justify-content:center}
.todo p{font-size:10px;line-height:13px;color:#3d4a52;margin:5px 0 4px 23px;text-align:justify}
.todo .go{font-size:11px;font-weight:700;color:#1d6f9e;margin-left:23px}
.main{left:274px;top:247px;width:762px;height:322px;background:var(--panel)}
.main .head{height:36px;background:linear-gradient(#39b6e6,#1e9bd3);color:#fff;font-size:21px;padding:6px 0 0 14px;border-bottom:2px solid #9fd5ea}
table{border-collapse:collapse;width:100%;table-layout:fixed;font-size:12px}
th{text-align:left;color:var(--navy);font-size:13px;height:28px;padding-left:10px;background:#fff;border-right:1px solid var(--panel-line)}
th.center{text-align:center;padding:0}
td{height:28px;padding-left:9px;border-right:1px solid var(--panel-line);border-top:1px solid var(--panel-line);background:#f1f8fb}
td a{color:var(--link)}
td.date{text-align:center;padding:0}
td.icons svg{vertical-align:middle;margin-right:9px}
tr.filler td{height:111px;background:var(--panel)}
.buttons{position:absolute;right:14px;bottom:14px;display:flex;gap:8px}
.btn{height:22px;border-radius:5px;font-size:10px;font-weight:700;color:#fff;display:flex;align-items:center;justify-content:center;background:linear-gradient(#b8e0f0,#8ec9e3);border:1px solid #8bc4dd}
.btn.primary{background:linear-gradient(#5cc6ee,#1f8fc6);border-color:#1c7fb0}
</style>
</head>
<body>
<div class="abs topbar"></div>
<div class="abs topbar-bottom"></div>

<div class="abs logo-box"><span class="logo-dot"></span><span class="logo-name">skylark</span></div>

<div class="abs account">
  Welcome <b>student@lms.skylark.nl</b>
  <div class="links">
    <svg width="14" height="12"><rect x="1" y="1" width="6" height="10" fill="#2d5f86"/><rect x="8" y="4" width="5" height="7" fill="#e4c36b"/></svg>
    Settings | Help | Sign out</div>
  <div class="msgs">
    <svg width="14" height="12"><rect x="1" y="2" width="12" height="9" fill="#f3efe0" stroke="#8a7"/><path d="M1 2l6 5 6-5" fill="none" stroke="#8a7"/></svg>
    4 new messages</div>
  <div class="meta">Server time : 6:46 AM<br>Last login ip : 192.168.0.15</div>
</div>

<div class="abs search">
  <div class="field">
    <svg width="10" height="10"><circle cx="4" cy="4" r="3" fill="none" stroke="#999"/><path d="M6 6l3 3" stroke="#999"/></svg>
    <span class="go">GO</span>
  </div>
  <div class="label">Search</div>
</div>

<div class="abs tab" style="left:13px;width:127px">Home</div>
<div class="abs tab active" style="left:142px;width:117px">Study Guide</div>
<div class="abs tab" style="left:262px;width:106px">Books</div>
<div class="abs tab" style="left:371px;width:82px">Tests</div>
<div class="abs tab" style="left:455px;width:111px">Results</div>

<nav class="abs subnav">
  <span><svg width="24" height="16"><rect x="1" y="2" width="6" height="13" fill="#e94b3c"/><rect x="8" y="2" width="6" height="13" fill="#f6c233"/><rect x="15" y="2" width="6" height="13" fill="#4caf50"/></svg>German</span>
  <span><svg width="24" height="16"><rect x="1" y="2" width="6" height="13" fill="#4caf50"/><rect x="8" y="2" width="6" height="13" fill="#f6c233"/><rect x="15" y="2" width="6" height="13" fill="#e94b3c"/></svg>Spanish</span>
  <span><svg width="24" height="16"><rect x="1" y="2" width="6" height="13" fill="#3b6fd1"/><rect x="8" y="2" width="6" height="13" fill="#e94b3c"/><rect x="15" y="2" width="6" height="13" fill="#f6c233"/></svg>French</span>
  <span><svg width="34" height="16"><rect x="1" y="3" width="28" height="11" rx="1" fill="#8bc34a" stroke="#4d7a1e"/><circle cx="15" cy="8.5" r="3" fill="#4d7a1e"/><circle cx="29" cy="12" r="4" fill="#f3c23a"/></svg>Economics</span>
  <span><svg width="14" height="18"><path d="M7 1C4 7 2 10 2 13a5 5 0 0010 0c0-3-2-6-5-12z" fill="#5aa9e6" stroke="#1f6ea8"/></svg>Chemistry</span>
</nav>

<section class="abs card clock">
  <div class="time">18:36</div>
  <div class="date">Thursday, 23rd December 2008</div>
  <div class="cal">
    <div class="month">‹&nbsp; December 2008 &nbsp;›</div>
    <div class="heads"><span>sun</span><span>mon</span><span>tue</span><span>wed</span><span>thu</span><span>fri</span><span>sat</span></div>
    <div class="grid">
      <span class="empty"></span><span>1</span><span>2</span><span>3</span><span>4</span><span>5</span><span>6</span>
      <span>7</span><span>8</span><span>9</span><span>10</span><span>11</span><span>12</span><span>13</span>
      <span>14</span><span>15</span><span>16</span><span>17</span><span>18</span><span>19</span><span>20</span>
      <span>21</span><span>22</span><span class="today">23</span><span>24</span><span>25</span><span>26</span><span>27</span>
      <span>28</span><span>29</span><span>30</span><span>31</span><span class="empty"></span><span class="empty"></span><span class="empty"></span>
    </div>
  </div>
</section>
<div class="abs event-row">
  <span><svg width="11" height="11"><rect x=".5" y=".5" width="10" height="10" fill="#cfe3ee" stroke="#4a86a8"/></svg>Add new event</span>
  <span><svg width="11" height="11"><rect x=".5" y=".5" width="10" height="10" fill="#cfe3ee" stroke="#4a86a8"/></svg>Next Event</span>
</div>

<aside class="abs card sidebar">
  <div class="box-head">Sidebar Menu</div>
  <ul>
    <li>Link 1</li><li>Link 2</li><li>Link 3</li><li>Link 4</li><li>Link 5</li><li>Link 6</li><li>Link 7</li>
  </ul>
</aside>

<aside class="abs card todo">
  <div class="box-head">To Do List</div>
  <div class="item">
    <div class="title"><span class="num">1</span>View new entries</div>
    <p>Lorem ipsum dolor sit amet, consectetur adipiscing elit. Vivamus sit amet elit pellentesque odio laoreet lacinia.</p>
    <div class="go">› Get Started</div>
  </div>
  <div class="item">
    <div class="title"><span class="num">2</span>Verify Scores</div>
    <p>Lorem ipsum dolor sit amet, consectetur adipiscing elit. Vivamus sit amet elit</p>
    <div class="go">› Get Started</div>
  </div>
  <div class="item" style="border:none">
    <div class="title"><span class="num">3</span>Test Comiing Up</div>
    <p>Lorem ipsum dolor sit amet, consectetur adipiscing elit. Vivamus sit amet elit pellentesque odio laoreet lacinia.</p>
    <div class="go">› Go</div>
  </div>
</aside>

<main class="abs card main">
  <div class="head">Study Guide Engels</div>
  <table>
    <colgroup><col style="width:104px"><col style="width:417px"><col style="width:95px"><col></colgroup>
    <thead><tr><th>Assignment</th><th>Description</th><th class="center">Deadline</th><th>Mark</th></tr></thead>
    <tbody>
      <tr><td><a>Opdracht 1</a></td><td>Engels opdracht 1 door leraar@lms.skylark.nl voor m2@lms.sk</td><td class="date">06/18/2008</td><td class="icons">
        <svg width="14" height="12"><path d="M1 3h5l1 1h6v7H1z" fill="#f5c542" stroke="#c9961c"/></svg><svg width="12" height="13"><circle cx="6" cy="4" r="3" fill="#6ab0d8"/><path d="M1 12c0-4 10-4 10 0z" fill="#3f88b8"/></svg><svg width="14" height="11"><rect x=".5" y="1.5" width="13" height="9" fill="#eee" stroke="#999"/><path d="M1 2l6 5 6-5" fill="none" stroke="#999"/></svg><svg width="11" height="11"><path d="M2 2l7 7M9 2l-7 7" stroke="#e0332a" stroke-width="2.5"/></svg><svg width="12" height="12"><rect x=".5" y=".5" width="11" height="11" fill="#fff" stroke="#557"/></svg></td></tr>
      <tr><td><a>Opdracht 2</a></td><td>Engels opdracht 2 door leraar@lms.skylark.nl voor m2@lms.sk</td><td class="date">06/18/2008</td><td class="icons">
        <svg width="14" height="12"><path d="M1 3h5l1 1h6v7H1z" fill="#f5c542" stroke="#c9961c"/></svg><svg width="12" height="13"><circle cx="6" cy="4" r="3" fill="#6ab0d8"/><path d="M1 12c0-4 10-4 10 0z" fill="#3f88b8"/></svg><svg width="14" height="11"><rect x=".5" y="1.5" width="13" height="9" fill="#eee" stroke="#999"/><path d="M1 2l6 5 6-5" fill="none" stroke="#999"/></svg><svg width="11" height="11"><path d="M2 2l7 7M9 2l-7 7" stroke="#e0332a" stroke-width="2.5"/></svg><svg width="12" height="12"><rect x=".5" y=".5" width="11" height="11" fill="#fff" stroke="#557"/></svg></td></tr>
      <tr><td><a>Opdracht 1</a></td><td>Engels opdracht 1 door leraar@lms.skylark.nl voor m2@lms.sk</td><td class="date">06/18/2008</td><td class="icons">
        <svg width="14" height="12"><path d="M1 3h5l1 1h6v7H1z" fill="#f5c542" stroke="#c9961c"/></svg><svg width="12" height="13"><circle cx="6" cy="4" r="3" fill="#6ab0d8"/><path d="M1 12c0-4 10-4 10 0z" fill="#3f88b8"/></svg><svg width="14" height="11"><rect x=".5" y="1.5" width="13" height="9" fill="#eee" stroke="#999"/><path d="M1 2l6 5 6-5" fill="none" stroke="#999"/></svg><svg width="11" height="11"><path d="M2 2l7 7M9 2l-7 7" stroke="#e0332a" stroke-width="2.5"/></svg><svg width="12" height="12"><rect x=".5" y=".5" width="11" height="11" fill="#fff" stroke="#557"/></svg></td></tr>
      <tr><td><a>Opdracht 2</a></td><td>Engels opdracht 2 door leraar@lms.skylark.nl voor m2@lms.sk</td><td class="date">06/18/2008</td><td class="icons">
        <svg width="14" height="12"><path d="M1 3h5l1 1h6v7H1z" fill="#f5c542" stroke="#c9961c"/></svg><svg width="12" height="13"><circle cx="6" cy="4" r="3" fill="#6ab0d8"/><path d="M1 12c0-4 10-4 10 0z" fill="#3f88b8"/></svg><svg width="14" height="11"><rect x=".5" y="1.5" width="13" height="9" fill="#eee" stroke="#999"/><path d="M1 2l6 5 6-5" fill="none" stroke="#999"/></svg><svg width="11" height="11"><path d="M2 2l7 7M9 2l-7 7" stroke="#e0332a" stroke-width="2.5"/></svg><svg width="12" height="12"><rect x=".5" y=".5" width="11" height="11" fill="#fff" stroke="#557"/></svg></td></tr>
      <tr class="filler"><td></td><td></td><td></td><td></td></tr>
    </tbody>
  </table>
  <div class="buttons">
    <div class="btn" style="width:91px">CHECK ALL</div>
    <div class="btn" style="width:106px">UNCHECK ALL</div>
    <div class="btn primary" style="width:80px">APPROVE</div>
  </div>
</main>

<div class="abs footer"></div>
</body>
</html>
```